Gourmet Restaurant Coffee Cup Print Design

We would like to redesign our coffee cup for our restaurant chain. Please visit our website at: www.dovrantis.ca.

Disposable Cup should be bilingual in English and French. We will provide translations. One side is to be french and the other English.

I have uploaded also the files that were provided to us by the cup manufacturer. These templates have all the necessary instructions.

Target Market(s)

Business Professionals, Millenials

Industry/Entity Type

Restaurant

Font styles to use
Serif
Sans Serif
Script

Requirements
Must have
• our entire logo or only the "TAVERINO'S" word in the logo.
• We are looking for 4 cup sizes with the same design but maybe a distinguishing color in each size of cup.
• We can provide cup templates in PDF along with full manufacturer instructions.
• We're looking for a simple clean design with a predominantly white background. The lid of the cup is white.
Nice to have
• Our motto or tag line is:
• A world of taste
Should not have
• photos only use illustrations

```html
<!DOCTYPE html>
<html lang="en">
<head>
<meta charset="utf-8">
<title>Taverino's – Cup Wrap</title>
<link rel="stylesheet" href="https://fonts.googleapis.com/css2?family=Jura:wght@400&family=Ultra&display=swap">
<style>
  :root {
    --navy: #170b5c;
    --crimson: #912827;
    --forest: #01582b;
    --saffron: #fcbb5b;
    --paper: #ffffff;
    --fold: #8a8a8a;
  }
  html, body {
    margin: 0;
    padding: 0;
    width: 1200px;
    height: 631px;
    overflow: hidden;
    background: var(--paper);
  }
  .cup-wrap {
    display: block;
    width: 1200px;
    height: 631px;
  }
  .ring { fill: none; }
  .ring--saffron { stroke: var(--saffron); stroke-width: 18; }
  .ring--saffron-wide { stroke: var(--saffron); stroke-width: 24; }
  .ring--crimson { stroke: var(--crimson); stroke-width: 20; }
  .ring--forest { stroke: var(--forest); stroke-width: 24; }
  .ring--navy { stroke: var(--navy); stroke-width: 16; }
  .dot--navy { fill: var(--navy); }
  .dot--crimson { fill: var(--crimson); }
  .dot--forest { fill: var(--forest); }
  .dot--saffron { fill: var(--saffron); }
  .fold-line { stroke: var(--fold); stroke-width: 1; }
  .wordmark {
    font-family: "Ultra", "Rockwell", "Georgia", serif;
    font-size: 100px;
    fill: var(--navy);
  }
  .tagline, .caution {
    font-family: "Jura", "Verdana", sans-serif;
  }
  .tagline--en { font-size: 32px; fill: var(--saffron); }
  .tagline--fr { font-size: 32px; fill: var(--crimson); }
  .caution--en { font-size: 16px; fill: var(--navy); }
  .caution--fr { font-size: 16px; fill: var(--forest); }
</style>
</head>
<body>
<svg class="cup-wrap" viewBox="0 0 1200 631" xmlns="http://www.w3.org/2000/svg" role="img" aria-label="Taverino's cup wrap: A world of taste / Un monde de goût">
  <defs>
    <path id="arc-tagline-en" d="M 160 225 A 260 260 0 0 1 520 225"/>
    <path id="arc-caution-en" d="M 230 400 A 200 200 0 0 0 470 400"/>
    <path id="arc-tagline-fr" d="M 680 420 A 300 300 0 0 0 1060 420"/>
    <path id="arc-caution-fr" d="M 760 215 A 200 200 0 0 1 1020 215"/>
  </defs>

  <g class="panel panel--english">
    <circle class="ring ring--saffron" cx="90" cy="120" r="70"/>
    <circle class="dot dot--crimson" cx="470" cy="90" r="36"/>
    <circle class="dot dot--saffron" cx="40" cy="420" r="18"/>
    <path class="ring ring--forest" d="M 50 560 A 110 110 0 0 1 140.9 451.7"/>
    <path class="ring ring--forest" d="M 179.1 451.7 A 110 110 0 0 1 270 560"/>
    <circle class="dot dot--navy" cx="520" cy="540" r="22"/>
    <text class="tagline tagline--en"><textPath href="#arc-tagline-en" startOffset="50%" text-anchor="middle">A world of taste</textPath></text>
    <text class="caution caution--en"><textPath href="#arc-caution-en" startOffset="50%" text-anchor="middle">Caution! May be hot!</textPath></text>
  </g>

  <line class="fold-line" x1="600" y1="0" x2="600" y2="631"/>

  <g class="panel panel--french">
    <path class="ring ring--navy" d="M 750 90 A 50 50 0 1 1 700 40"/>
    <circle class="ring ring--crimson" cx="1110" cy="110" r="60"/>
    <circle class="dot dot--forest" cx="720" cy="560" r="34"/>
    <circle class="dot dot--navy" cx="960" cy="560" r="16"/>
    <path class="ring ring--saffron-wide" d="M 1020 640 A 110 110 0 0 1 1110.9 531.7"/>
    <path class="ring ring--saffron-wide" d="M 1149.1 531.7 A 110 110 0 0 1 1240 640"/>
    <text class="tagline tagline--fr"><textPath href="#arc-tagline-fr" startOffset="50%" text-anchor="middle">Un monde de goût</textPath></text>
    <text class="caution caution--fr"><textPath href="#arc-caution-fr" startOffset="50%" text-anchor="middle">Prudence! Peut être chaud!</textPath></text>
  </g>

  <text class="wordmark" x="600" y="345" text-anchor="middle" textLength="820" lengthAdjust="spacingAndGlyphs">TAVERINO'S</text>
</svg>
</body>
</html>
```